Design business card using existing logo.

PLEASE DO NOT USE "RED WHITE & BLACK" color combo! Thank you.

Try different color combos such as:
- Vintage colors like brown, orange, gold, blue (not all together but a combo of 1 or 3
- Blue, w/ grey, or silver or white, Blue monochromatic can work as well.
- Use monochromatic variations on back (just an idea)

- Include full name, "Quillmark Records" on at least one side.

Target Market(s)

Teens

Industry/Entity Type

Business

Colors
3277b5
ffc214
f04a50
f78f20

```html
<!DOCTYPE html>
<html lang="en">
<head>
<meta charset="utf-8">
<title>Quillmark Records business card</title>
<link href="https://fonts.googleapis.com/css2?family=Lato:wght@300;400&display=swap" rel="stylesheet">
<style>
  :root {
    --backdrop: #2b2b2b;
    --card: #1d1d1d;
    --card-edge: #262626;
    --mark: #8c8c8c;
    --mark-faint: #262626;
    --text-strong: #9a9a9a;
    --text-soft: #7c7c7c;
  }
  * { box-sizing: border-box; margin: 0; padding: 0; }
  html, body {
    width: 1200px; height: 716px; overflow: hidden;
    background: var(--backdrop);
    font-family: "Lato", sans-serif;
  }
  .sheet {
    width: 1200px; height: 716px;
    display: flex; align-items: center; justify-content: center; gap: 60px;
  }
  .card {
    position: relative;
    width: 510px; height: 300px;
    background: var(--card);
    border: 1px solid var(--card-edge);
    border-radius: 6px;
    box-shadow: 0 14px 30px rgba(0,0,0,.45);
    overflow: hidden;
  }
  /* front */
  .front-halo {
    position: absolute; left: 105px; top: 10px;
    width: 280px; height: 280px; border-radius: 50%;
    background: var(--mark-faint);
  }
  .front-brand {
    position: absolute; inset: 0;
    display: flex; flex-direction: column; align-items: center; justify-content: center;
    gap: 10px;
  }
  .brand-dot {
    width: 96px; height: 96px; border-radius: 50%;
    background: var(--mark);
  }
  .brand-name {
    font-weight: 300; font-size: 34px; letter-spacing: 1px;
    color: var(--mark); text-transform: uppercase;
  }
  .brand-sub {
    font-weight: 300; font-size: 13px; letter-spacing: 9px;
    color: var(--mark); text-transform: uppercase; margin-top: -8px;
  }
  .front-web {
    font-size: 15px; color: var(--text-soft); margin-top: 4px;
  }
  /* back */
  .back-brand {
    position: absolute; left: 40px; top: 60px; width: 230px;
    display: flex; flex-direction: column; align-items: center; gap: 14px;
  }
  .back-brand .brand-dot { width: 110px; height: 110px; }
  .back-brand .brand-name { font-size: 30px; }
  .contact {
    position: absolute; left: 300px; top: 95px;
    color: var(--text-soft);
  }
  .contact-name { font-size: 24px; color: var(--text-strong); }
  .contact-title { font-size: 13px; margin-bottom: 18px; }
  .contact-line {
    display: flex; align-items: center; gap: 10px;
    font-size: 15px; margin-bottom: 12px;
  }
  .contact-line svg { width: 14px; height: 14px; fill: none; stroke: var(--text-soft); stroke-width: 1.6; }
</style>
</head>
<body>
<main class="sheet">
  <section class="card card-front">
    <div class="front-halo"></div>
    <div class="front-brand">
      <div class="brand-dot"></div>
      <div class="brand-name">Quillmark</div>
      <div class="brand-sub">Records</div>
      <div class="front-web">yourwebsite.com</div>
    </div>
  </section>

  <section class="card card-back">
    <div class="back-brand">
      <div class="brand-dot"></div>
      <div class="brand-name">Quillmark</div>
    </div>
    <div class="contact">
      <div class="contact-name">Your Name</div>
      <div class="contact-title">Job Title</div>
      <div class="contact-line">
        <svg viewBox="0 0 16 16"><path d="M3 2h3l1.5 3.5-2 1.2a9 9 0 0 0 3.8 3.8l1.2-2L14 10v3a1.5 1.5 0 0 1-1.5 1.5A11 11 0 0 1 1.5 3.5 1.5 1.5 0 0 1 3 2z"/></svg>
        000 000 0000
      </div>
      <div class="contact-line">
        <svg viewBox="0 0 16 16"><rect x="1.5" y="3.5" width="13" height="9"/><path d="M1.5 3.5 8 9l6.5-5.5"/></svg>
        youremail@xyz.com
      </div>
      <div class="contact-line">
        <svg viewBox="0 0 16 16"><circle cx="8" cy="8" r="6.5"/><ellipse cx="8" cy="8" rx="3" ry="6.5"/><path d="M1.5 8h13"/></svg>
        yourwebsite.com
      </div>
    </div>
  </section>
</main>
</body>
</html>
```